VELMORAN RECORDS
New independent record label
VELMORAN RECORDS -
Creative Brief
www.velmoranrecords.co.uk
independent record label
we are open to your thoughts and designs.
Modern
Red used in the logo for the background colour
below header
www.plintonrecords.co.uk
www.quaystreetjournal.com
www.brindlewick.co.uk
we would like a banner in the header that slideshows the signed artists with a small text biography.

```html
<!DOCTYPE html>
<html lang="en">
<head>
<meta charset="utf-8">
<title>Velmoran Records</title>
<link href="https://fonts.googleapis.com/css2?family=Arimo:wght@400;700&display=swap" rel="stylesheet">
<style>
:root{
  --bg:#1c1c1c;
  --bg-dark:#121212;
  --panel:#232323;
  --red:#d8121b;
  --red-dark:#8e0a10;
  --white:#ffffff;
  --grey:#b9b9b9;
  --muted:#7c7c7c;
  --line:#3a3a3a;
}
*{margin:0;padding:0;box-sizing:border-box}
html,body{width:1200px;height:1052px;overflow:hidden}
body{background:var(--bg);font-family:"Arimo",Arial,sans-serif;color:var(--white);position:relative}
.abs{position:absolute}

.header{left:0;top:0;width:1200px;height:150px;background:linear-gradient(#262626,#1a1a1a)}
.brand{left:150px;top:18px;display:flex;align-items:center;gap:14px}
.brand-mark{width:80px;height:80px;border-radius:50%;background:linear-gradient(#e9e9e9,#8d8d8d)}
.brand-name{font-size:34px;font-weight:700;letter-spacing:1px;color:var(--white);line-height:1}
.search{left:876px;top:12px;width:180px;height:28px;display:flex}
.search-field{flex:1;background:#f1f1f1;border:1px solid #999;color:#888;font-size:12px;padding:6px 8px}
.search-btn{width:28px;background:var(--red);display:flex;align-items:center;justify-content:center}

.nav{left:150px;top:112px;display:flex;gap:34px;font-size:17px}
.nav a{color:var(--white);text-decoration:none;padding-bottom:6px}
.nav a.active{border-bottom:3px solid var(--red)}

.band{left:0;top:152px;width:1200px;height:378px;background:linear-gradient(var(--red-dark),var(--red) 20%,var(--red) 80%,var(--red-dark))}
.slider{left:150px;top:176px;width:904px;height:346px;border:3px solid #111;border-radius:6px;overflow:hidden;background:linear-gradient(120deg,#f4f4f4 0%,#d9d9d9 30%,#9c8fa4 55%,#5a4a5c 80%,#2a2a2a 100%)}
.headline{left:20px;top:16px;font-weight:700;font-size:44px;line-height:50px;color:#111}
.headline .red{color:var(--red)}
.caption{left:0;bottom:0;width:100%;height:72px;background:rgba(0,0,0,.72);padding:10px 18px;font-size:12.5px;line-height:17px;color:#ddd;padding-right:300px}
.learn{right:14px;bottom:22px}
.dots{left:160px;top:510px;display:flex;gap:6px}
.dots i{width:7px;height:7px;border-radius:50%;background:#777}
.dots i.on{background:#eee}

.pill{display:inline-flex;align-items:center;gap:10px;height:38px;padding:0 18px 0 6px;border-radius:20px;font-weight:700;font-size:19px;color:var(--white)}
.pill.red{background:var(--red)}
.pill.dark{background:#0e0e0e;border:1px solid #444}
.pill .play{width:26px;height:26px;border-radius:50%;background:var(--white);display:flex;align-items:center;justify-content:center}
.pill.small{height:32px;font-size:15px;gap:8px}
.pill.small .play{width:22px;height:22px}

.col{top:542px}
.col-title{display:flex;align-items:center;gap:10px;font-size:26px;color:#ddd;height:40px;border-bottom:1px solid var(--line)}
.col-title .rule{flex:1;height:2px;background:#555}
.news{left:160px;width:282px}
.news-item{margin-top:14px;font-size:13px;line-height:17px}
.news-item .date{font-weight:700;color:var(--white)}
.news-item.first .date{color:var(--red)}
.news-item p{color:var(--grey)}
.music{left:464px;width:272px}
.video{left:762px;width:282px}
.feature{margin-top:14px;height:148px;border:3px solid #ddd;background:linear-gradient(#6a6a6a,#1e1e1e)}
.cap{font-size:12.5px;color:var(--grey);margin-top:6px}
.thumbs{display:flex;gap:12px;margin-top:14px}
.thumb{flex:1}
.thumb .ph{height:88px;border:3px solid #ddd;background:linear-gradient(#5c5c5c,#1b1b1b)}
.more{top:925px}

.footer{left:0;top:975px;width:1200px;height:77px;background:var(--bg-dark);border-top:1px solid var(--line)}
.foot-links{left:160px;top:14px;font-size:13px;color:var(--grey)}
.copy{left:160px;top:36px;font-size:11.5px;color:var(--muted)}
.social{left:950px;top:20px;display:flex;gap:6px}
.social i{width:24px;height:24px;background:#ddd;border-radius:3px}
</style>
</head>
<body>
<header class="header abs">
  <div class="brand abs"><div class="brand-mark"></div><div class="brand-name">VELMORAN RECORDS</div></div>
  <div class="search abs"><div class="search-field">Search...</div><div class="search-btn"><svg width="14" height="14" viewBox="0 0 14 14"><circle cx="6" cy="6" r="4" fill="none" stroke="#fff" stroke-width="2"/><line x1="9" y1="9" x2="13" y2="13" stroke="#fff" stroke-width="2"/></svg></div></div>
  <nav class="nav abs"><a class="active">Home</a><a>Music</a><a>Video</a><a>Featured</a><a>Tour</a><a>Executives</a><a>Blog</a><a>Contact</a></nav>
</header>

<div class="band abs"></div>
<section class="slider abs" role="img" aria-label="Group photo of a signed band posed in front of a graffiti wall">
  <div class="headline abs">Lorem Ipsum Dolor Sit Amet<br>of Lorem Ipsum Dolor Sit<br><span class="red">Lorem Ipsum Dolor Sit Amet<br>and Ipsum</span></div>
  <div class="caption abs">Lorem ipsum dolor sit amet, consectetur adipiscing elit, sed diam nonummy nibh euismod tincidunt ut laoreet dolore magna aliquam erat volutpat. Ut wisi enim ad minim veniam, quis nostrud exerci tation ullamcorper suscipit lobortis nisl ut aliquip ex ea commodo consequat.</div>
  <div class="learn abs"><span class="pill red"><span class="play"><svg width="12" height="12" viewBox="0 0 12 12"><path d="M3 1l8 5-8 5z" fill="#d8121b"/></svg></span>Learn More</span></div>
</section>
<div class="dots abs"><i class="on"></i><i></i><i></i><i></i></div>

<section class="col news abs">
  <div class="col-title"><svg width="22" height="22" viewBox="0 0 22 22"><rect x="2" y="3" width="18" height="16" fill="none" stroke="#ccc" stroke-width="2"/><line x1="6" y1="9" x2="16" y2="9" stroke="#ccc" stroke-width="2"/><line x1="6" y1="13" x2="16" y2="13" stroke="#ccc" stroke-width="2"/></svg>News Update</div>
  <div class="news-item first"><div class="date">29/02/2011 - Preorder now</div><p>The Happy Birthday EP is now availible to pre-order.</p></div>
  <div class="news-item"><div class="date">29/02/2011 - Preorder now</div><p>The Happy Birthday EP is now availible to pre-order.</p></div>
  <div class="news-item"><div class="date">29/02/2011 - Preorder now</div><p>The Happy Birthday EP is now availible to pre-order.</p></div>
  <div class="news-item"><div class="date">29/02/2011 - Preorder now</div><p>The Happy Birthday EP is now availible to pre-order.</p></div>
  <div class="news-item"><div class="date">29/02/2011 - Preorder now</div><p>The Happy Birthday EP is now availible to pre-order.</p></div>
</section>

<section class="col music abs">
  <div class="col-title"><span class="rule"></span>Top Music<span class="rule"></span></div>
  <div class="feature" role="img" aria-label="Band portrait for featured track"></div>
  <div class="cap">Lorem ipsum dolor sit - Sit amet</div>
  <div class="thumbs">
    <div class="thumb"><div class="ph" role="img" aria-label="Artist photo"></div><div class="cap">Lorem ipsum dolor sit - Sit amet</div></div>
    <div class="thumb"><div class="ph" role="img" aria-label="Artist photo"></div><div class="cap">Lorem ipsum dolor sit - Sit amet</div></div>
  </div>
</section>

<section class="col video abs">
  <div class="col-title"><span class="rule"></span>Top Video<span class="rule"></span></div>
  <div class="feature" role="img" aria-label="Still from featured music video"></div>
  <div class="cap">Lorem ipsum dolor sit - Sit amet</div>
  <div class="thumbs">
    <div class="thumb"><div class="ph" role="img" aria-label="Video still"></div><div class="cap">Lorem ipsum dolor sit - Sit amet</div></div>
    <div class="thumb"><div class="ph" role="img" aria-label="Video still"></div><div class="cap">Lorem ipsum dolor sit - Sit amet</div></div>
  </div>
</section>

<div class="more abs" style="left:160px"><span class="pill red small"><span class="play"><svg width="10" height="10" viewBox="0 0 12 12"><path d="M3 1l8 5-8 5z" fill="#d8121b"/></svg></span>More News</span></div>
<div class="more abs" style="left:464px"><span class="pill red small"><span class="play"><svg width="10" height="10" viewBox="0 0 12 12"><path d="M3 1l8 5-8 5z" fill="#d8121b"/></svg></span>More Music</span></div>
<div class="more abs" style="left:762px"><span class="pill dark small"><span class="play"><svg width="10" height="10" viewBox="0 0 12 12"><path d="M3 1l8 5-8 5z" fill="#111"/></svg></span>More Video</span></div>

<footer class="footer abs">
  <div class="foot-links abs">Home | Music | Video | Featured | Tour | Executives | Blog | About Us | Contact</div>
  <div class="copy abs">© 2011 Velmoran Records Ltd. All rights reserved.</div>
  <div class="social abs"><i></i><i></i><i></i></div>
</footer>
</body>
</html>
```